Paper Lantern Theory - Podcast Cover

Paper Lantern Theory is a weekly podcast that dispels some of the myths about conventional economic thinking and provides a new way of thinking about issues that are faced by the global economy. It's insightful, thought-provoking and, most importantly, fun. We are refreshing the look and sound of the podcast. I have attached a copy of the old amateur design (which I did!)

Target Market(s)

Male oriented, smart folk with an interest in politics and economics

Font styles to use
Sans Serif

Requirements
Must have
• Clearly visible title, even when reduced in size. Must be 3000 pixels by 3000 pixels.
Nice to have
• This podcast challenges the status quo. It should reflect that. Photos and names of the hosts. Actually, because th ephotos are so different, we'd be open to the idea of a caricature if you can do that within the price.

```html
<!DOCTYPE html>
<html lang="en">
<head>
<meta charset="utf-8">
<title>Paper Lantern Theory Podcast – Cover Set</title>
<link href="https://fonts.googleapis.com/css2?family=Montserrat:wght@700;800&display=swap" rel="stylesheet">
<style>
  :root {
    --ink: #000000;
    --paper: #ffffff;
    --ember: #d9440f;
    --tan-light: #d8c293;
    --tan-dark: #b8936a;
    --teal-shadow: #0f3b3a;
    --grey-light: #d6d6d6;
    --grey-dark: #7a7a7a;
    --cover-bg: var(--ink);
    --cover-line: var(--paper);
    --cover-title: var(--ember);
    --cover-bar: var(--ember);
    --cover-accent: var(--ember);
    --host-a: linear-gradient(160deg, var(--tan-light) 0%, var(--tan-dark) 45%, var(--ember) 75%, var(--teal-shadow) 100%);
    --host-b: linear-gradient(160deg, var(--tan-light) 0%, var(--tan-light) 55%, var(--ember) 85%, var(--teal-shadow) 100%);
  }
  * { box-sizing: border-box; margin: 0; padding: 0; }
  html, body { width: 1200px; height: 900px; overflow: hidden; background: var(--paper); }
  body { position: relative; font-family: "Montserrat", Arial, sans-serif; }

  .cover {
    position: absolute;
    width: 900px; height: 900px;
    background: var(--cover-bg);
    overflow: hidden;
  }
  .cover--main { left: 0; top: 0; }

  .cover__kicker, .cover__title-line, .cover__suffix {
    position: absolute; left: 0; right: 0;
    text-align: center; font-weight: 800; line-height: 1;
    white-space: nowrap;
  }
  .cover__kicker { top: 21px; font-size: 62px; color: var(--cover-line); }
  .cover__title-line { color: var(--cover-title); }
  .cover__title-line--one { top: 100px; font-size: 90px; letter-spacing: -1px; }
  .cover__title-line--two { top: 196px; font-size: 150px; letter-spacing: 6px; }
  .cover__suffix { top: 335px; font-size: 64px; color: var(--cover-line); }

  .host-art { position: absolute; top: 412px; height: 400px; }
  .host-art--left { left: 38px; width: 440px; background: var(--host-a); border-radius: 46% 46% 0 0 / 34% 34% 0 0; }
  .host-art--right { left: 472px; width: 392px; background: var(--host-b); border-radius: 44% 44% 0 0 / 32% 32% 0 0; }

  .host-intro {
    position: absolute; left: 360px; width: 200px; top: 528px;
    text-align: center; color: var(--cover-accent);
    font-weight: 700; font-size: 27px; line-height: 1.15;
  }

  .host-bar {
    position: absolute; left: 0; right: 0; bottom: 0; height: 88px;
    background: var(--cover-bar); color: var(--paper);
    font-weight: 700; font-size: 30px;
  }
  .host-bar span { position: absolute; top: 28px; transform: translateX(-50%); white-space: nowrap; }
  .host-bar .host-name--a { left: 243px; }
  .host-bar .host-join { left: 450px; font-size: 34px; top: 24px; }
  .host-bar .host-name--b { left: 690px; }

  .thumb {
    position: absolute; left: 913px;
    width: 274px; height: 274px;
    border: 1px solid var(--ink);
    overflow: hidden;
  }
  .thumb--dark { top: 17px; }
  .thumb--light { top: 313px; }
  .thumb--mono { top: 608px; }
  .thumb .cover { left: 0; top: 0; transform: scale(0.3022); transform-origin: top left; }

  .cover--light { --cover-bg: var(--paper); --cover-line: var(--ink); }
  .cover--mono {
    --cover-bg: var(--paper); --cover-line: var(--ink); --cover-title: var(--ink);
    --cover-bar: var(--ink); --cover-accent: var(--ink);
    --host-a: linear-gradient(160deg, var(--grey-light) 0%, var(--grey-dark) 70%, #3a3a3a 100%);
    --host-b: linear-gradient(160deg, var(--grey-light) 0%, var(--grey-light) 60%, var(--grey-dark) 100%);
  }
</style>
</head>
<body>

<section class="cover cover--main">
  <p class="cover__kicker">THE</p>
  <h1 class="cover__title-line cover__title-line--one">PAPER LANTERN</h1>
  <p class="cover__title-line cover__title-line--two">THEORY</p>
  <p class="cover__suffix">PODCAST</p>
  <div class="host-art host-art--left" role="img" aria-label="Posterised illustration of the first host, smiling, in a polo shirt"></div>
  <div class="host-art host-art--right" role="img" aria-label="Posterised illustration of the second host, wearing glasses and a t-shirt"></div>
  <p class="host-intro">WITH<br>YOUR HOSTS</p>
  <div class="host-bar"><span class="host-name--a">MILES HARROW</span><span class="host-join">&amp;</span><span class="host-name--b">PROF. OWEN TARRANT</span></div>
</section>

<div class="thumb thumb--dark">
  <section class="cover">
    <p class="cover__kicker">THE</p>
    <p class="cover__title-line cover__title-line--one">PAPER LANTERN</p>
    <p class="cover__title-line cover__title-line--two">THEORY</p>
    <p class="cover__suffix">PODCAST</p>
    <div class="host-art host-art--left" role="img" aria-label="Illustration of the first host"></div>
    <div class="host-art host-art--right" role="img" aria-label="Illustration of the second host"></div>
    <p class="host-intro">WITH<br>YOUR HOSTS</p>
    <div class="host-bar"><span class="host-name--a">MILES HARROW</span><span class="host-join">&amp;</span><span class="host-name--b">PROF. OWEN TARRANT</span></div>
  </section>
</div>

<div class="thumb thumb--light">
  <section class="cover cover--light">
    <p class="cover__kicker">THE</p>
    <p class="cover__title-line cover__title-line--one">PAPER LANTERN</p>
    <p class="cover__title-line cover__title-line--two">THEORY</p>
    <p class="cover__suffix">PODCAST</p>
    <div class="host-art host-art--left" role="img" aria-label="Illustration of the first host"></div>
    <div class="host-art host-art--right" role="img" aria-label="Illustration of the second host"></div>
    <p class="host-intro">WITH<br>YOUR HOSTS</p>
    <div class="host-bar"><span class="host-name--a">MILES HARROW</span><span class="host-join">&amp;</span><span class="host-name--b">PROF. OWEN TARRANT</span></div>
  </section>
</div>

<div class="thumb thumb--mono">
  <section class="cover cover--mono">
    <p class="cover__kicker">THE</p>
    <p class="cover__title-line cover__title-line--one">PAPER LANTERN</p>
    <p class="cover__title-line cover__title-line--two">THEORY</p>
    <p class="cover__suffix">PODCAST</p>
    <div class="host-art host-art--left" role="img" aria-label="Greyscale illustration of the first host"></div>
    <div class="host-art host-art--right" role="img" aria-label="Greyscale illustration of the second host"></div>
    <p class="host-intro">WITH<br>YOUR HOSTS</p>
    <div class="host-bar"><span class="host-name--a">MILES HARROW</span><span class="host-join">&amp;</span><span class="host-name--b">PROF. OWEN TARRANT</span></div>
  </section>
</div>

</body>
</html>
```